Motivational Poster Design Project

I would like to create a poster with some of my favorite quotes to hang in my office.

Industry/Entity Type

Quotes

Requirements
Must have
• The poster will be 24" high x 36" long and printed on canvas, so the image you create needs to have a resolution of at least 2700 x 3900.

The poster must contain the following quotes:

“Your beliefs become your thoughts,
Your thoughts become your words,
Your words become your actions,
Your actions become your habits,
Your habits become your values,
Your values become your destiny.”
-Tavish Orlanno

"Winners practice until they get it right. Champions practice until they can’t get it wrong!"
-Unknown

"Style is the perfection of a point of view."
-Leopold Quimsby

"My interest in life comes from setting myself huge, apparently unachieveable challenges and trying to rise above them."
-Sir Edmund Valcourt

"Problems cannot be solved by the same level of thinking that created them."
-Bertram Holloway

"People think focus means saying yes to the thing you've got to focus on. But that's not what it means at all. It means saying no to the hundred other good ideas that there are. You have to pick carefully."
-Dale Morcum

"Think like a man of action and act like a man of thought."
-Lucien Fravel
Nice to have
• It would be nice to have an image of each person who is being quoted (if known) along with the quote that is attributable to them.

```html
<!DOCTYPE html>
<html lang="en">
<head>
<meta charset="utf-8">
<title>Motivational Poster</title>
<link rel="stylesheet" href="https://fonts.googleapis.com/css2?family=Patrick+Hand+SC&display=swap">
<style>
:root{
  --page:#ffffff;
  --paper:#f7f6f3;
  --ink:#2a2622;
  --bubble:#fdfcf8;
  --tan:#a89a84;    --tan-ink:#6a5d4a;
  --green:#8fcf4d;  --green-ink:#3f7a1c;
  --purple:#a77fae; --purple-ink:#6a4a73;
  --salmon:#e0977a; --salmon-ink:#8a4a34;
  --blue:#6f84b3;   --blue-ink:#34415f;
  --red:#d84a1a;    --red-ink:#b3360e;
  --orange:#e8a15a; --orange-ink:#a85f1e;
  --grey-tone:#a39e93;
  --purple-tone:#a98bc0;
  --green-tone:#8fd14a;
  --salmon-tone:#e3977c;
  --blue-tone:#7f93c4;
  --orange-tone:#f0a050;
}
*{box-sizing:border-box;margin:0;padding:0}
html,body{width:1200px;height:900px;overflow:hidden;background:var(--page)}
body{position:relative;font-family:"Patrick Hand SC",cursive}
.poster{position:absolute;left:32px;top:82px;width:1136px;height:756px;background:var(--paper);overflow:hidden;border:1px solid #e4e2dc}
.tails{position:absolute;left:0;top:0;width:1136px;height:756px}
.portrait{position:absolute;border-radius:46% 46% 0 0/30% 30% 0 0}
.portrait--fravel{left:0;top:366px;width:205px;height:337px;background:linear-gradient(#b8b3a8,var(--grey-tone) 60%,#7d786e)}
.portrait--holloway{left:173px;top:398px;width:265px;height:305px;background:linear-gradient(#c1a6d3,var(--purple-tone) 60%,#8a6ca2)}
.portrait--orlanno{left:418px;top:448px;width:250px;height:255px;background:linear-gradient(#a8e070,var(--green-tone) 60%,#6fb032)}
.portrait--morcum{left:618px;top:358px;width:200px;height:345px;background:linear-gradient(#eeb09a,var(--salmon-tone) 60%,#c97a60)}
.portrait--valcourt{left:758px;top:348px;width:220px;height:355px;background:linear-gradient(#9cacd4,var(--blue-tone) 60%,#5d71a3)}
.portrait--quimsby{left:928px;top:408px;width:208px;height:295px;background:linear-gradient(#f6bb7a,var(--orange-tone) 60%,#d2813a)}
.names{position:absolute;left:0;top:703px;width:1136px;height:53px;background:var(--paper);border-top:1px solid #d8d5cc}
.name{position:absolute;top:12px;font-size:25px;letter-spacing:-.5px;color:var(--ink)}
.name--fravel{left:10px;color:#5e574c}
.name--holloway{left:180px;color:#6a4a73}
.name--orlanno{left:420px;color:#3f7a1c}
.name--morcum{left:622px;color:#8a4a34}
.name--valcourt{left:768px;color:#34415f}
.name--quimsby{left:982px;color:#a85f1e}
.bubble{position:absolute;background:var(--bubble);border:5px solid;border-radius:12px;box-shadow:3px 3px 0 var(--ink);padding:6px 16px;font-size:21px;line-height:24px;text-transform:uppercase}
.bubble--fravel{left:26px;top:44px;width:382px;height:70px;border-color:var(--tan);color:var(--tan-ink)}
.bubble--orlanno{left:60px;top:114px;width:420px;height:172px;border-color:var(--green);color:var(--green-ink)}
.bubble--holloway{left:223px;top:300px;width:363px;height:96px;border-color:var(--purple);color:var(--purple-ink);padding-left:30px}
.bubble--morcum{left:471px;top:6px;width:385px;height:162px;font-size:20px;line-height:23px;border-color:var(--salmon);color:var(--salmon-ink)}
.bubble--valcourt{left:590px;top:174px;width:466px;height:86px;border-color:var(--blue);color:var(--blue-ink)}
.bubble--champions{left:873px;top:60px;width:253px;height:106px;border-color:var(--red);color:var(--red-ink);font-size:19px;line-height:21px;padding:8px 12px}
.bubble--quimsby{left:841px;top:268px;width:287px;height:64px;border-color:var(--orange);color:var(--orange-ink);padding:4px 14px}
</style>
</head>
<body>
<main class="poster">
  <svg class="tails" viewBox="0 0 1136 756" aria-hidden="true">
    <g stroke-width="5" fill="var(--bubble)" stroke-linejoin="round">
      <path d="M48 110 Q60 260 76 350 Q86 250 110 110" stroke="var(--tan)"/>
      <path d="M440 282 Q560 340 580 420 Q540 330 470 282" stroke="var(--green)"/>
      <path d="M400 392 L418 438 L440 392" stroke="var(--purple)"/>
      <path d="M520 164 Q600 300 658 372 Q610 270 580 164" stroke="var(--salmon)"/>
      <path d="M700 256 Q740 330 768 372 Q760 320 750 256" stroke="var(--blue)"/>
      <path d="M1020 328 L1038 404 L1058 328" stroke="var(--orange)"/>
    </g>
  </svg>

  <div class="portrait portrait--fravel" role="img" aria-label="Drawn portrait of Lucien Fravel in grey tones"></div>
  <div class="portrait portrait--holloway" role="img" aria-label="Drawn portrait of Bertram Holloway in purple tones"></div>
  <div class="portrait portrait--orlanno" role="img" aria-label="Drawn portrait of Tavish Orlanno in green tones"></div>
  <div class="portrait portrait--morcum" role="img" aria-label="Drawn portrait of Dale Morcum in salmon tones"></div>
  <div class="portrait portrait--valcourt" role="img" aria-label="Drawn portrait of Sir Edmund Valcourt in blue tones"></div>
  <div class="portrait portrait--quimsby" role="img" aria-label="Drawn portrait of Leopold Quimsby in orange tones"></div>

  <p class="bubble bubble--fravel">Think like a man of action<br>and act like a man of thought.</p>
  <p class="bubble bubble--orlanno">Your beliefs become your thoughts,<br>your thoughts become your words,<br>your words become your actions,<br>your actions become your habits,<br>your habits become your values,<br>your values become your destiny.</p>
  <p class="bubble bubble--holloway">Problems cannot be solved<br>by the same level of thinking<br>that created them.</p>
  <p class="bubble bubble--morcum">People think focus means saying yes<br>to the thing you’ve got to focus on.<br>But that’s not what it means at all.<br>It means saying no to the hundred<br>other good ideas that there are.<br>You have to pick carefully.</p>
  <p class="bubble bubble--valcourt">My interest in life comes from setting myself<br>huge, apparently unachievable challenges<br>and trying to rise above them.</p>
  <p class="bubble bubble--champions">Winners practice until<br>they get it right.<br>Champions practice until<br>they can’t get it wrong!</p>
  <p class="bubble bubble--quimsby">Style is the perfection<br>of a point of view.</p>

  <footer class="names">
    <span class="name name--fravel">Lucien Fravel</span>
    <span class="name name--holloway">Bertram Holloway</span>
    <span class="name name--orlanno">Tavish Orlanno</span>
    <span class="name name--morcum">Dale Morcum</span>
    <span class="name name--valcourt">Sir Edmund Valcourt</span>
    <span class="name name--quimsby">Leopold Quimsby</span>
  </footer>
</main>
</body>
</html>
```